Redesign Call Answering Service Company Website

There is a good explanation of what we do at existing website deskbellhelpers.com.au.

We are getting traffic and now want to increase conversions and reduce drop offs. We need to create trust very quickly.

Once website done we will be looking to redesign logo.

We want to use “F” shaped reading pattern for website viewers. 2 very rough ideas on attached wireframes docs. The winning site only needs to follow the rough layout – no need for boxes, etc. Looking for creative help here!

One page needed (home page) that easily becomes all other pages without a "price reference" (see wire frames).

All existing pages will have new/updated content added with extra pages added.

Target Market(s)

Target market to appeal to is 70% females 25 to 60, self-employed business owners, complimentary/alternative therapists, small to medium business ente

Industry/Entity Type

It Company

Requirements
Must have
• must have items on wire frames
must have a Client Login (to self-service area)
must have a Contact Area with 4 x phone numbers, 1 x fax number and email/contact us

```html
<!DOCTYPE html>
<html lang="en">
<head>
<meta charset="utf-8">
<title>Desk Bell Helpers – Phone Answering</title>
<link href="https://fonts.googleapis.com/css2?family=Ubuntu:ital,wght@0,400;0,500;0,700;1,400;1,700&family=Tinos:wght@400;700&display=swap" rel="stylesheet">
<style>
:root{
  --blue:#1346c4;
  --blue-dark:#0b2f95;
  --blue-light:#2a9be8;
  --green:#6cc417;
  --green-dark:#3a9a10;
  --green-light:#9ee334;
  --text:#333;
  --muted:#555;
  --line:#d6d6d6;
  --page:#f1f1f1;
}
*{box-sizing:border-box;margin:0;padding:0}
html,body{width:1144px;height:1200px;overflow:hidden;background:#fff}
body{font-family:"Ubuntu",sans-serif;color:var(--text);position:relative}
.abs{position:absolute}
.site{position:absolute;left:50px;top:0;width:1040px;height:1200px;background:#fff;box-shadow:0 0 6px rgba(0,0,0,.15)}
.header-band{left:50px;top:0;width:1040px;height:152px;background:linear-gradient(#fff,#e9e9e9);border-bottom:1px solid #ddd}
.brand{left:85px;top:26px;display:flex;align-items:center;gap:14px}
.brand-dot{width:70px;height:70px;border-radius:50%;background:var(--blue)}
.brand-name{font-weight:700;font-size:36px;line-height:38px;color:var(--blue)}
.hotline{left:688px;top:3px;display:flex;align-items:center;gap:6px;font-style:italic;font-size:24px;color:#777}
.hotline svg{width:36px;height:36px}
.client-login{left:930px;top:0;width:113px;height:34px;border-radius:0 0 8px 8px;background:linear-gradient(#4db8f5,var(--blue));color:#fff;font-weight:500;font-size:14px;text-align:center;line-height:30px;box-shadow:0 2px 3px rgba(0,0,0,.3)}
.tag-top{left:668px;top:60px;font-weight:700;font-size:20px;color:var(--blue)}
.tag-main{left:668px;top:82px;font-weight:700;font-size:34px;color:var(--green-dark)}
.nav{left:83px;top:129px;width:973px;height:40px;border-radius:14px;background:linear-gradient(#2a8ee6,var(--blue-dark));display:flex;align-items:center;overflow:hidden}
.nav a{color:#fff;text-decoration:none;font-size:14px;padding:0 24px;height:40px;line-height:40px}
.nav a.current{background:linear-gradient(var(--green-light),var(--green-dark));width:90px;text-align:center;padding:0}
.cities{left:105px;top:182px;display:flex;align-items:center;gap:22px;font-size:18px;font-weight:500;color:var(--blue)}
.cities b{color:var(--green-dark);font-style:italic;font-weight:700}
.cities svg{width:32px;height:32px}
.hero{left:73px;top:227px;width:726px;height:317px;background:linear-gradient(90deg,#fff,#f2f2f2);border:1px solid #e2e2e2}
.features{left:90px;top:240px;width:402px;height:290px;background:rgba(255,255,255,.9);border:1px solid #e6e6e6;list-style:none;padding-top:16px}
.features li{height:28px;display:flex;align-items:center;font-size:12.5px;color:#333;padding-left:12px}
.features li::before{content:">";width:14px;height:13px;margin-right:17px;background:var(--green);color:#fff;font-size:10px;text-align:center;line-height:13px}
.hero-photo{left:492px;top:228px;width:307px;height:316px;background:radial-gradient(circle at 60% 40%,#e8c9ae,#b98c6e 45%,#e8e8e8 80%)}
.price{left:812px;top:177px;width:243px;height:224px;border-radius:14px;border:3px solid #fff;box-shadow:0 0 4px rgba(0,0,0,.25);background:linear-gradient(var(--green-light),#52b60c);text-align:center;color:#fff;overflow:hidden}
.price .from{font-style:italic;font-size:17px;margin-top:8px}
.price .amount{font-weight:700;font-size:62px;line-height:60px}
.price .per{font-weight:700;font-size:20px;margin-top:-4px}
.price .trial{margin:10px auto 0;width:154px;height:40px;background:linear-gradient(#fff,#dcdcdc);color:var(--green-dark);font-weight:700;font-size:22px;line-height:40px}
.price .plans{position:absolute;left:0;bottom:0;width:100%;height:56px;background:linear-gradient(#4ca80c,#7ad62a);font-weight:700;font-size:22px;line-height:56px}
.card{background:#fff;border:1px solid var(--line);border-radius:14px}
.blog{left:814px;top:425px;width:243px;height:302px}
.heading{font-family:"Tinos",serif;color:var(--blue);font-size:24px}
.blog-icon{left:823px;top:432px;width:46px;height:46px;border-radius:50%;background:#f07b22;border:3px solid #fff;box-shadow:0 0 3px rgba(0,0,0,.3)}
.date{left:806px;top:490px;width:69px;height:64px;background:linear-gradient(var(--blue),var(--blue-light));color:#fff;font-family:"Tinos",serif;text-align:center;line-height:18px;padding-top:2px}
.date .day{font-size:28px;font-weight:700;line-height:26px}
.blog-title{left:884px;top:488px;width:165px;font-weight:700;font-size:14px;line-height:18px;color:var(--blue)}
.blog-body{left:826px;top:573px;width:223px;font-size:12px;line-height:18px;color:var(--muted);text-align:justify}
.posted{left:826px;top:673px;font-family:Arial,sans-serif;font-size:12px}
.posted b{color:#e0420e}
.share{left:828px;top:703px;font-family:Arial,sans-serif;font-size:12px;display:flex;align-items:center;gap:4px}
.share i{width:16px;height:16px;background:#666;display:inline-block}
.plus{width:26px;height:34px;background:linear-gradient(#4a6ee6,var(--blue-dark));color:#fff;font-size:20px;text-align:center;line-height:40px;clip-path:polygon(50% 0,100% 25%,100% 100%,0 100%,0 25%)}
.questions{left:89px;top:570px;width:708px;height:181px;border-radius:30px}
.q-list{list-style:none;font-size:13px;color:#555;letter-spacing:.3px}
.q-list li{height:24px;display:flex;align-items:center}
.q-list li::before{content:"»";color:var(--blue);font-size:16px;margin-right:12px}
.testimonials{left:89px;top:764px;width:340px;height:215px}
.quote{left:117px;top:835px;width:292px;font-family:"Tinos",serif;font-weight:700;font-size:14px;line-height:24px;color:#444;text-align:justify}
.quote-by{left:118px;top:940px;font-family:"Tinos",serif;font-style:italic;font-weight:700;font-size:15px;color:var(--blue)}
.boxes-icon{width:40px;height:40px}
.video{left:447px;top:768px;width:345px;height:211px;background:#cfe3f5;border:1px solid #9cc3e6;padding:5px}
.video-screen{width:100%;height:185px;background:linear-gradient(#fff,#f0f0f0);position:relative;border:1px solid #ccc}
.video-photo{position:absolute;left:110px;top:10px;width:150px;height:175px;background:radial-gradient(circle at 50% 35%,#e9c8aa,#c49677 40%,#f4f4f4 75%)}
.video-brand{position:absolute;left:20px;top:18px;font-weight:700;font-size:13px;color:var(--blue)}
.video-bar{width:100%;height:14px;background:#222;margin-top:2px;position:relative}
.video-bar span{position:absolute;left:22px;top:5px;width:220px;height:3px;background:#555}
.video-bar span::before{content:"";position:absolute;left:0;top:0;width:108px;height:3px;background:#e01e1e}
.ask{left:814px;top:746px;width:246px;height:233px}
.field-label{font-size:13px;color:#333}
.field{background:#fff;border:1px solid #bbb;box-shadow:inset 0 1px 2px rgba(0,0,0,.15)}
.send{left:982px;top:948px;width:73px;height:27px;border-radius:14px;background:linear-gradient(#3e8ff0,var(--blue-dark));color:#fff;font-size:14px;text-align:center;line-height:27px}
.footer{left:63px;top:993px;width:1015px;height:167px;background:linear-gradient(#1ea3ec,var(--blue))}
.foot-col{top:1008px}
.foot-col h3{font-family:"Tinos",serif;font-weight:700;font-size:22px;color:#fff;margin-bottom:12px}
.foot-col h3 span{color:var(--green-light)}
.foot-col ul{list-style:none}
.foot-col li{font-size:13px;color:#fff;height:28px}
.foot-col li::before{content:"* ";}
.contact{left:690px;top:1003px;width:359px;height:143px;border:2px solid #9ed2f6;border-radius:14px}
.contact p{font-family:Arial,sans-serif;font-weight:700;font-size:12.5px;color:#fff;line-height:20px}
.mail-icon{left:953px;top:1041px;width:66px;height:64px;border-radius:10px;background:linear-gradient(#fff,#ccc)}
.copyright-band{left:63px;top:1160px;width:1015px;height:36px;background:linear-gradient(var(--green-light),var(--green-dark))}
.copyright{left:85px;top:1170px;font-style:italic;font-weight:700;font-size:11px;color:#fff}
.follow{left:840px;top:1168px;display:flex;align-items:center;gap:10px;font-size:13px;color:#fff}
.follow i{width:22px;height:22px;border-radius:4px;background:rgba(255,255,255,.85);display:inline-block}
</style>
</head>
<body>
<div class="site"></div>

<header>
  <div class="abs header-band"></div>
  <div class="abs brand"><span class="brand-dot"></span><span class="brand-name">Desk Bell<br>Helpers</span></div>
  <div class="abs hotline">
    <svg viewBox="0 0 36 36"><circle cx="18" cy="18" r="16" fill="none" stroke="#777" stroke-width="2.5"/><path d="M13 10c-2 1-3 3-1 7s5 8 9 9c3 1 4-1 4-2l-3-3-2 1c-2-1-4-4-5-6l1-2-3-4z" fill="#777"/></svg>
    1300 555 018
  </div>
  <div class="abs client-login">Client Login</div>
  <div class="abs tag-top">Be Confident your phones are covered</div>
  <div class="abs tag-main">whatever you are doing</div>
  <nav class="abs nav">
    <a class="current">Home</a><a>Phone Answering</a><a>Virtual Reception</a><a>FAQ</a><a>About Us</a><a>Free Trial</a>
  </nav>
</header>

<div class="abs cities">
  <svg viewBox="0 0 32 32"><circle cx="16" cy="16" r="14" fill="none" stroke="#888" stroke-width="2"/><path d="M11 8c-2 1-3 3-1 7s5 8 9 9c3 1 4-1 4-2l-3-3-2 1c-2-1-4-4-5-6l1-2-3-4z" fill="var(--green-dark)"/></svg>
  <span><b>Sydney</b> (02) 5550 1182</span>
  <span><b>Melbourne</b> (03) 5550 2273</span>
  <span><b>Brisbane</b> (07) 5550 3364</span>
</div>

<section>
  <div class="abs hero"></div>
  <div class="abs hero-photo" role="img" aria-label="Photo of a smiling receptionist wearing a headset"></div>
  <ul class="abs features">
    <li>Properly trained Australian based operators</li>
    <li>Simple to use. No software to download or IT skills needed</li>
    <li>Calls answered professionally in your company name</li>
    <li>Flexible and customisable answering processes</li>
    <li>Calls screened to your rules</li>
    <li>Important people always put through, you control</li>
    <li>Callers introduced before transfer</li>
    <li>Messages sent to email and/or text</li>
    <li>Messages can be sent to multiple people</li>
    <li>Dedicated local numbers Australia wide</li>
  </ul>
</section>

<aside class="abs price">
  <div class="from">From as little as:</div>
  <div class="amount">$4.90</div>
  <div class="per">per week</div>
  <div class="trial">FREE TRIAL ➤</div>
  <div class="plans">Plans &amp; Pricing</div>
</aside>

<aside>
  <div class="abs card blog"></div>
  <div class="abs blog-icon"></div>
  <div class="abs heading" style="left:878px;top:438px">Recent Blogpost</div>
  <div class="abs date">April<div class="day">07</div>2012</div>
  <div class="abs blog-title">Lorem ipsum dolor sit amet, consectetur adipiscing elit.</div>
  <p class="abs blog-body">Curabitur dictum, arcu eget gravida mollis, mauris augue adipiscing enim, vel luctus odio augue in dui. Nunc eleifend lectus id turpis posuere tincidunt. In lectus tortor...</p>
  <div class="abs posted">[ <b>Posted By :</b> Web Studio North ]</div>
  <div class="abs share">Share This <i></i><i></i><i></i><i></i></div>
  <div class="abs plus" style="left:1009px;top:696px">+</div>
</aside>

<section>
  <div class="abs card questions"></div>
  <ul class="abs q-list" style="left:130px;top:585px">
    <li>Phones causing stress?</li><li>Too many voicemails?</li><li>Callers not leaving messages?</li><li>Callers getting busy tone?</li><li>Missing important calls?</li><li>Missing leads or opportunities?</li>
  </ul>
  <ul class="abs q-list" style="left:410px;top:585px">
    <li>Phones causing stress?</li><li>Too many voicemails?</li><li>Callers not leaving messages?</li><li>Callers getting busy tone?</li><li>Missing important calls?</li><li>Missing leads or opportunities?</li>
  </ul>
</section>

<section>
  <div class="abs card testimonials"></div>
  <svg class="abs boxes-icon" style="left:101px;top:783px" viewBox="0 0 40 40"><g fill="none" stroke="var(--blue)" stroke-width="3"><rect x="2" y="14" width="16" height="16" rx="3"/><rect x="14" y="4" width="16" height="16" rx="3"/><rect x="20" y="18" width="16" height="16" rx="3"/></g></svg>
  <div class="abs heading" style="left:148px;top:788px">Testimonials</div>
  <div class="abs" style="left:95px;top:826px;font-family:Tinos,serif;font-size:34px;color:#aaa">“</div>
  <p class="abs quote">We have used Callwell for over 25 Years. We feel they have given us competitive pricing, dependable service and have been responsive to our needs <span style="color:#aaa;font-size:24px">”</span></p>
  <div class="abs quote-by">Fern Brothers</div>
  <div class="abs plus" style="left:377px;top:947px">+</div>
</section>

<section class="abs video">
  <div class="video-screen">
    <div class="video-brand">Voice Desk</div>
    <div class="video-photo" role="img" aria-label="Video still of a call centre agent with a headset"></div>
  </div>
  <div class="video-bar"><span></span></div>
</section>

<aside>
  <div class="abs card ask"></div>
  <svg class="abs boxes-icon" style="left:826px;top:762px" viewBox="0 0 40 40"><g fill="none" stroke="var(--blue)" stroke-width="3"><rect x="2" y="14" width="16" height="16" rx="3"/><rect x="14" y="4" width="16" height="16" rx="3"/><rect x="20" y="18" width="16" height="16" rx="3"/></g></svg>
  <div class="abs heading" style="left:876px;top:767px">Ask us anything !</div>
  <div class="abs field-label" style="left:836px;top:824px">Name</div>
  <div class="abs field" style="left:877px;top:820px;width:177px;height:27px"></div>
  <div class="abs field-label" style="left:838px;top:864px">Email</div>
  <div class="abs field" style="left:877px;top:858px;width:177px;height:27px"></div>
  <div class="abs field-label" style="left:817px;top:904px">Question</div>
  <div class="abs field" style="left:877px;top:897px;width:177px;height:45px"></div>
  <div class="abs send">Send</div>
</aside>

<footer>
  <div class="abs footer"></div>
  <div class="abs foot-col" style="left:97px"><h3><span>Other</span> Links</h3><ul><li>Home</li><li>Phone Answering</li><li>Dairy Management</li><li>Plands and Pricing</li></ul></div>
  <div class="abs foot-col" style="left:298px"><h3><span>Other</span> Links</h3><ul><li>Home</li><li>Phone Answering</li><li>Dairy Management</li><li>Plands and Pricing</li></ul></div>
  <div class="abs foot-col" style="left:504px"><h3><span>Other</span> Links</h3><ul><li>Home</li><li>Phone Answering</li><li>Dairy Management</li><li>Plands and Pricing</li></ul></div>
  <div class="abs contact"></div>
  <div class="abs foot-col" style="left:708px;top:1008px"><h3><span>Contact</span> Us</h3></div>
  <div class="abs contact" style="border:none;left:710px;top:1041px;width:240px;height:auto">
    <p>Desk Bell Helpers Pty Ltd</p><p>ABN: 00 000 000 000</p><p>Unit 4, 22 Harbour St</p><p>Lane Grove, NSW 2099</p><p>info@deskbellhelpers.com.au</p>
  </div>
  <svg class="abs mail-icon" viewBox="0 0 66 64"><rect x="2" y="2" width="62" height="60" rx="10" fill="#f4f4f4" stroke="#bbb"/><rect x="12" y="18" width="42" height="28" fill="none" stroke="var(--blue)" stroke-width="4"/><path d="M12 18l21 16 21-16" fill="none" stroke="var(--blue)" stroke-width="4"/></svg>
  <div class="abs copyright-band"></div>
  <div class="abs copyright">Copyright (C) desk bell helpers 1968 - 2012.  All Rights Reserved</div>
  <div class="abs follow">Follow Us On :- <i></i><i></i><i></i><i></i></div>
</footer>
</body>
</html>
```